Radiant Sound Productions "Beneath Silver Skies concert"

I need a poster for advertising a concert as part of the Harbourlight Culture Festival in Western Australia.
THE POSTER SHOULD BE SOFT, ROMANTIC AND SENSUAL (not sexy).

This concert will be the launch of my new album "beneath Silver Skies" it is a piano and vocal concert on Stage at the Corvell Civic Hall.

The music is classical crossover in style, operatic, but very soft and intimate. With a warm inviting vocal sound that should draw the listener in and feel sensual. Many of the songs will be well known to the audience but they will not have heard them before in these new intimate arrangements.
I have attached a sample of one of the songs. This is one of the softer tracks. others have a bit more movement and a subtle beat.

The image with pearls has been used by me for other events so is familiar to those who have come to my concerts before. I am happy for you to change the background colour and definition.
I would like something romantic that references operatic/classical/baroque music but also shows that we have updated the songs and made them more appealing to a wider audience.
My musical influences are Helen Marsdale, Rosalind Haverty, Ylvana but I feel our arrangements are more interesting being piano based.

****************************
Radiant Sound Productions
Delia Corwen
and Teodoro Valenti - Piano

"Beneath Silver Skies" Album Launch
Corvell Civic Hall
Sunday 3rd November 2013
Matinee 3:00pm

Beautiful arias and original songs from Delia's newly released album, with musical arrangements by Teodoro Valenti. A uniquely soft and intimate concert with everything performed "Beneath Silver Skies" only for you.

Tickets www.seatquarry.example.au
Tel: 1300 518 907
Further info
www.deliacorwen.example.com
Friendspace Delia Corwen Concert Club

STANDARD $45 Upstairs Gallery
PREMIUM $95 Seated at tables with wine and gourmet basket from organic caterers - Willow Larder.

Target Market(s)

definately the over 55's classical music lovers who go to concerts regularly.

Industry/Entity Type

Advertising

Requirements
Must have
• Harbourlight Culture Logo

```html
<!DOCTYPE html>
<html lang="en">
<head>
<meta charset="utf-8">
<title>Beneath Silver Skies – Delia Corwen in Concert</title>
<link href="https://fonts.googleapis.com/css2?family=Great+Vibes&family=Poiret+One&family=Raleway:wght@300;400;500&display=swap" rel="stylesheet">
<style>
  :root {
    --paper: #f4f2ef;
    --paper-soft: #fbfaf8;
    --silk: #e6e3de;
    --gold: #d98a1e;
    --gold-deep: #b8690f;
    --copper: #9a6a3c;
    --ink: #574a40;
    --ink-soft: #7b716a;
    --muted: #8f8983;
    --band: #f3e9c4;
    --rule: #b9b1a8;
    --white: #ffffff;
    --black: #1d1a18;
  }
  html, body { margin: 0; padding: 0; overflow: hidden; background: var(--paper); }
  .poster {
    position: relative;
    width: 849px;
    height: 1200px;
    overflow: hidden;
    background:
      radial-gradient(ellipse at 75% 20%, var(--paper-soft) 0%, transparent 60%),
      linear-gradient(160deg, var(--silk) 0%, var(--paper) 35%, var(--paper-soft) 60%, var(--silk) 100%);
    font-family: "Raleway", sans-serif;
  }
  .presenter {
    position: absolute;
    top: 66px; left: 0; width: 856px;
    text-align: center;
    font-weight: 300;
    font-size: 19px;
    line-height: 27px;
    color: var(--muted);
    margin: 0;
  }
  .title {
    position: absolute;
    top: 100px; left: 0; width: 849px; height: 260px;
    margin: 0;
    font-family: "Great Vibes", cursive;
    font-weight: 400;
    color: var(--gold);
    text-shadow: 0 1px 0 var(--gold-deep);
  }
  .title span { position: absolute; white-space: nowrap; }
  .title .word-one { left: 60px; top: 70px; font-size: 130px; }
  .title .word-two { left: 345px; top: 20px; font-size: 116px; }
  .portrait {
    position: absolute;
    left: 0; top: 420px;
    width: 520px; height: 680px;
    background:
      radial-gradient(ellipse at 38% 22%, #e9cdbb 0%, #b48060 22%, transparent 45%),
      radial-gradient(ellipse at 70% 68%, #f0c9c3 0%, transparent 22%),
      linear-gradient(180deg, transparent 0%, #8a5a3a 45%, #6e4128 70%, #3a2418 100%);
    -webkit-mask-image: linear-gradient(90deg, #000 70%, transparent 100%);
            mask-image: linear-gradient(90deg, #000 70%, transparent 100%);
  }
  .blurb {
    position: absolute;
    top: 350px; left: 448px; width: 392px;
    margin: 0;
    text-align: center;
    font-family: "Poiret One", sans-serif;
    font-size: 19.5px;
    line-height: 31px;
    color: var(--copper);
    font-weight: 400;
  }
  .rule { position: absolute; height: 1px; background: var(--rule); }
  .rule.top { top: 678px; left: 408px; width: 407px; }
  .rule.bottom { top: 829px; left: 450px; width: 280px; }
  .event {
    position: absolute;
    top: 694px; left: 395px; width: 440px;
    text-align: center;
    color: var(--ink);
  }
  .event p { margin: 0; font-size: 35px; line-height: 44px; font-weight: 300; letter-spacing: 0.5px; white-space: nowrap; }
  .event strong { font-weight: 500; }
  .event sup { font-size: 17px; vertical-align: 15px; }
  .tickets {
    position: absolute;
    top: 868px; left: 520px; width: 320px;
    text-align: center;
    font-size: 19px;
    line-height: 24.5px;
    color: var(--ink-soft);
    font-weight: 400;
  }
  .tickets p { margin: 0; }
  .price-band {
    position: absolute;
    left: 0; top: 1086px; width: 849px; height: 114px;
    background: linear-gradient(180deg, rgba(243,233,196,0) 0%, var(--band) 25%, var(--band) 100%);
  }
  .prices {
    position: absolute;
    top: 1103px; left: 148px; width: 690px;
    margin: 0;
    font-size: 17px;
    line-height: 23px;
    color: var(--ink-soft);
  }
  .council-tab {
    position: absolute;
    left: 30px; top: 872px;
    width: 103px; height: 328px;
    background: var(--white);
  }
  .council-mark {
    position: absolute;
    top: 42px; left: 0; width: 103px;
    text-align: center;
    font-size: 11px;
    line-height: 13px;
    font-weight: 500;
    color: var(--black);
  }
  .council-mark .dot {
    display: block;
    width: 22px; height: 22px;
    margin: 0 auto 6px;
    border-radius: 50%;
    background: var(--black);
  }
  .council-divider {
    position: absolute;
    top: 118px; left: 20px; width: 63px;
    border-top: 1px dashed var(--black);
  }
  .festival-tag {
    position: absolute;
    top: 128px; left: 80px;
    transform-origin: 0 0;
    transform: rotate(90deg);
    white-space: nowrap;
    font-size: 17px;
    line-height: 19px;
    color: var(--black);
    font-weight: 400;
  }
  .festival-tag b { font-weight: 500; }
</style>
</head>
<body>
<main class="poster">
  <p class="presenter">Radiant Sound Productions<br>Delia Corwen and Teodoro Valenti - Piano</p>

  <h1 class="title"><span class="word-two">Silver Skies</span><span class="word-one">Beneath</span></h1>

  <div class="portrait" role="img" aria-label="Photograph of the singer with pearls in her hair, reclining on an upright piano with a bouquet of pale pink roses"></div>

  <p class="blurb">Beautiful arias and original songs from Delia's newly released album, with musical arrangements by Teodoro Valenti. A uniquely soft and intimate concert with everything performed Beneath Silver Skies only for you.</p>

  <div class="rule top"></div>
  <section class="event">
    <p><strong>CORVELL CIVIC HALL</strong></p>
    <p>SUNDAY <strong>3<sup>RD</sup> NOVEMBER</strong></p>
    <p>MATINEE <strong>3:00PM</strong></p>
  </section>
  <div class="rule bottom"></div>

  <section class="tickets">
    <p>Tickets</p>
    <p>www.seatquarry.example.au</p>
    <p>Tel: 1300 518 907</p>
    <p>Further info</p>
    <p>www.deliacorwen.example.com</p>
    <p>Friendspace</p>
    <p>Delia Corwen Concert Club</p>
  </section>

  <div class="price-band"></div>
  <p class="prices">STANDARD $45 Upstairs Gallery<br>PREMIUM $95 Seated at tables with wine and gourmet basket<br>from organic caterers - Willow Larder.</p>

  <aside class="council-tab">
    <div class="council-mark"><span class="dot"></span>City of<br>Corvell Bay</div>
    <div class="council-divider"></div>
    <div class="festival-tag">A CITY OF<br>CORVELL BAY<br><b>FESTIVAL EVENT</b></div>
  </aside>
</main>
</body>
</html>
```